Einladungskarten-Design für Ehepaar
Zielgruppe
Wir sind ein Ehepaar und feiern 2 Geburtstage und eine Hochzeit in einem grossen Fest. Unsere Zielgruppe sind unsere Freunde.
Aufgabenstellung
Doppelkarte A5 quer, nur Frontseite designed; Briefing siehe Worddok

```html
<!DOCTYPE html>
<html lang="de">
<head>
<meta charset="utf-8">
<title>Einladung – Dreifach Grund zu feiern</title>
<link rel="stylesheet" href="https://fonts.googleapis.com/css2?family=Archivo:wght@400;500&family=Open+Sans:wght@400&family=Roboto:wght@500;700&display=swap">
<style>
  :root {
    --paper: #efeae2;
    --forest: #1b7650;
    --forest-deep: #15603f;
    --leaf: #6dbf56;
    --lime: #2bb04a;
    --white: #ffffff;
  }
  * { margin: 0; padding: 0; box-sizing: border-box; }
  html, body {
    width: 1200px; height: 904px; overflow: hidden;
    background: var(--paper);
  }
  .card {
    position: absolute; left: 20px; top: 57px;
    width: 1160px; height: 790px;
    overflow: hidden; background: var(--white);
  }
  .jungle-photo {
    position: absolute; inset: 0;
    background:
      radial-gradient(ellipse 40% 35% at 30% 62%, rgba(255,255,255,0.85), rgba(255,255,255,0) 70%),
      radial-gradient(ellipse 30% 25% at 22% 8%, rgba(255,255,255,0.9), rgba(255,255,255,0) 70%),
      linear-gradient(160deg, var(--forest) 0%, #4d9a74 35%, #e9f2ed 55%, var(--forest) 80%, var(--forest-deep) 100%);
  }
  .headline {
    position: absolute; left: 187px; top: 78px;
    font-family: "Archivo", sans-serif; font-weight: 400;
    font-size: 66px; letter-spacing: 1px; line-height: 1;
    color: var(--forest);
  }
  .headline .accent { color: var(--lime); }
  .reasons {
    position: absolute; left: 162px; top: 146px;
    width: 447px; height: 167px;
    background: var(--forest);
    padding: 10px 0 0 23px;
    font-family: "Archivo", sans-serif; font-weight: 500;
    font-size: 26px; line-height: 36px; color: var(--white);
    list-style: none;
  }
  .badges { position: absolute; inset: 0; width: 1160px; height: 790px; }
  .badge-text {
    position: absolute; color: var(--white); text-align: center;
    transform: translate(-50%, -50%); white-space: nowrap;
  }
  .badge-decades { left: 604px; top: 326px; font-family: "Roboto", sans-serif; font-weight: 500; font-size: 58px; }
  .badge-date { left: 468px; top: 430px; font-family: "Roboto", sans-serif; font-weight: 500; font-size: 28px; }
  .badge-years { left: 928px; top: 204px; font-family: "Roboto", sans-serif; font-weight: 700; font-size: 122px; }
  .occasions {
    position: absolute; left: 843px; top: 283px;
    font-family: "Open Sans", sans-serif; font-size: 18px; line-height: 1; color: var(--white);
  }
  .occasions .count { font-size: 28px; }
  .occasions .row-birthdays { display: block; }
  .occasions .row-wedding { display: block; margin-left: 14px; margin-top: -6px; }
</style>
</head>
<body>
  <main class="card">
    <div class="jungle-photo" role="img" aria-label="Zweifarbiges Foto eines Bananenhains mit großen Blättern in Dunkelgrün und Weiß"></div>

    <h1 class="headline"><span class="accent">EIN</span>LADUNG</h1>

    <ul class="reasons">
      <li>DREIFACH GRUND ZU FEIERN</li>
      <li>DOPPELTER GEBURTSTAG</li>
      <li>EINE HOCHZEIT</li>
      <li>FEST AM 6.10.2018</li>
    </ul>

    <svg class="badges" viewBox="0 0 1160 790" aria-hidden="true">
      <circle cx="609" cy="326" r="118" fill="var(--forest)"/>
      <circle cx="604" cy="328" r="82" fill="var(--leaf)"/>
      <circle cx="468" cy="430" r="43" fill="var(--leaf)"/>
      <circle cx="949" cy="206" r="200" fill="var(--forest)"/>
      <circle cx="928" cy="206" r="180" fill="var(--leaf)"/>
    </svg>

    <div class="badge-text badge-decades">6x10</div>
    <div class="badge-text badge-date">6.10.</div>
    <div class="badge-text badge-years">60x2</div>

    <p class="occasions">
      <span class="row-birthdays"><span class="count">2</span>Geburtstage</span>
      <span class="row-wedding"><span class="count">1</span> Hochzeit</span>
    </p>
  </main>
</body>
</html>
```